Cellular Repair Retail Store Flyer/Postcards

We are looking for a good flyer for us to print and distribute as well as post on various web sites. Our company name is "Handset Fixit Crew" and we repair a wide range of cellular phones from Zelphones to Zelpads, Varnok's,,QT's, Brivanta, and PWD. In general if you have a cell phone we repair it. Cellular repairs is the primary focus however we are also an accessory superstore with 1'000's of choices of phone cases for all model phones. Historically these phone cases have all been aftermarket however now there are a number of brands. I'll attach a few so we have the ability to use some branded logo's on the flyer. Not all the graphics need to be used that we are providing. Again the flyer's main objective is, 1) Cellular Repairs, 2) Our location & pic of building (I have one attached but i'll have a new one within 24 hours and 3) Cellular Accessory Superstore with 1,000's of case. The address to our location is 4817 N 19th Street, Milwaukee, Wisconsin 53209. Anytime we use our address we state "2 Blocks North of 19th & Pemberly" (popular intersection in the market). So i'm not sure what approach to go... but I figured i'd provide a bunch of stuff for you to pick from. Naturally let's not make the flyer too busy but if we hit the 3 main deal points we will be good. Attached are; some pics of attractive phone cases, a few cellular accessory brands such as Heron Shell, Valdoro, Skinmitten, LuVenn, Cragmore etc. These logo's may add a nice appeal given they are national companies. For your reference and to be listed on the flyer is our web site; www.handsetfixitcrew.example

Requirements
Must have
• This advertisement will be used for the Postal Porchdrop Bulk Mailer so we need to make the flyer with the following measurements in mind; 6.25" x 9"
Nice to have
• In addition to repairing phones we need to promote we buy used and broken smart phones. Repairs done on site with certified technicians.

```html
<!DOCTYPE html>
<html lang="en">
<head>
<meta charset="utf-8">
<title>Handset Fixit Crew Flyers</title>
<link rel="stylesheet" href="https://fonts.googleapis.com/css2?family=Anton&family=Roboto+Condensed:wght@400;700&display=swap">
<style>
:root{
  --blue:#3f7fd6;
  --blue-deep:#2f68bb;
  --blue-light:#6aa2e6;
  --ink:#2c3440;
  --grey:#5a6270;
  --paper:#ffffff;
  --bg-top:#cfe6fa;
  --bg-bottom:#6fb2ee;
}
*{box-sizing:border-box;margin:0;padding:0}
html,body{width:1200px;height:1000px;overflow:hidden}
body{background:linear-gradient(160deg,var(--bg-top),var(--bg-bottom));font-family:"Roboto Condensed",sans-serif;position:relative}
.flyer{position:absolute;top:190px;width:430px;height:621px;background:var(--paper);overflow:hidden;box-shadow:0 10px 30px rgba(20,60,120,.25)}
.flyer--accessory{left:140px}
.flyer--repair{left:630px}
.abs{position:absolute}
.display{font-family:"Anton",sans-serif;text-transform:uppercase;line-height:.95;letter-spacing:.5px}
.photo{position:absolute}

/* accessory side */
.storefront{left:0;top:0;width:430px;height:252px;background:linear-gradient(180deg,#7e9ec9 0%,#c9ccd1 45%,#8c8f96 75%,#5b6a84 100%)}
.address-box{left:0;top:150px;width:165px;height:88px;background:var(--blue);color:#fff;padding:14px 14px;font-size:13px}
.location-box{left:228px;top:145px;width:202px;height:158px;background:var(--blue);color:#fff;padding:14px 14px}
.location-box .l1{font-size:19px}
.location-box .l2{font-size:36px;margin-top:4px}
.location-box .l3{font-size:19px}
.location-box .l4{font-size:31px}
.accessory-headline{left:18px;top:262px;color:var(--blue)}
.accessory-headline .big{font-size:44px}
.accessory-headline .mid{font-size:28px;color:var(--blue-light)}
.accessory-headline .dark{font-size:28px;color:var(--ink)}
.case-photo{left:14px;top:410px;width:205px;height:114px;background:linear-gradient(135deg,#2b2e34,#6e7580 55%,#a9c7e8);border-radius:6px}
.accessory-copy{left:238px;top:318px;width:178px}
.accessory-copy h3{font-family:"Anton",sans-serif;font-weight:400;font-size:12px;color:var(--ink);text-transform:uppercase;line-height:1.15;margin-bottom:5px}
.accessory-copy p{font-size:9.5px;color:var(--grey);line-height:1.3}
.brand-list{left:238px;top:430px;width:180px;display:flex;flex-wrap:wrap;gap:6px}
.brand{font-family:"Roboto Condensed",sans-serif;font-weight:700;font-size:11px;color:var(--ink);border:1px solid #c9d2de;padding:4px 6px;display:flex;align-items:center;gap:5px}
.brand i{width:8px;height:8px;background:var(--ink);display:inline-block}
.band{left:0;width:430px;background:var(--blue);color:#fff}
.flyer--accessory .band{top:532px;height:89px}
.site{left:16px;bottom:18px;font-size:15px}
.phone-block{right:18px;bottom:14px;text-align:right}
.phone-block .label{font-size:18px}
.phone-block .number{font-size:24px;margin-top:2px}

/* repair side */
.logo{left:24px;top:20px;display:flex;align-items:center;gap:8px;color:var(--blue-deep);font-family:"Anton",sans-serif;font-size:27px}
.logo i{width:16px;height:16px;border-radius:50%;background:var(--blue-deep);display:inline-block}
.repair-headline{left:22px;top:82px;color:var(--blue)}
.repair-headline .small{font-size:27px}
.repair-headline .huge{font-size:74px}
.handsets-photo{left:288px;top:78px;width:128px;height:70px;background:linear-gradient(135deg,#1d2430,#4e7fc0 60%,#c9dbf0);border-radius:4px}
.repair-copy{left:272px;top:158px;width:148px;font-size:9px;color:var(--grey);line-height:1.3}
.repair-copy .intro{color:var(--ink);font-weight:700;font-size:10px;margin-bottom:6px}
.repair-copy h3{font-family:"Anton",sans-serif;font-weight:400;font-size:11px;color:var(--ink);text-transform:uppercase;line-height:1.15;margin:6px 0 3px}
.phones-photo{left:24px;top:255px;width:232px;height:262px;background:linear-gradient(160deg,#e8edf3,#9aa6b5 50%,#3c4655);border-radius:8px}
.badge{left:176px;top:300px;width:78px;height:78px;border-radius:50%;background:var(--blue-light);color:#fff;font-size:9.5px;line-height:1.2;text-align:center;display:flex;align-items:center;justify-content:center;padding:7px}
.buy-banner{left:0;top:392px;width:256px;height:24px;background:var(--blue-light);color:#fff;font-size:11px;display:flex;align-items:center;justify-content:center}
.hand-photo{left:292px;top:352px;width:118px;height:62px;background:radial-gradient(ellipse at center,#c9a68e,#6f7580 70%,#f2f4f7 100%);border-radius:40%}
.service-list{left:272px;top:424px;width:150px;list-style:none}
.service-list li{display:flex;gap:6px;font-family:"Anton",sans-serif;font-size:10.5px;color:var(--ink);text-transform:uppercase;line-height:1.15;margin-bottom:6px}
.service-list svg{flex:none;margin-top:1px}
.flyer--repair .band{top:540px;height:81px}
.repair-phone{left:22px;top:10px}
.repair-phone .label{font-size:22px}
.repair-phone .number{font-size:28px;margin-top:2px}
</style>
</head>
<body>

<section class="flyer flyer--accessory">
  <div class="photo storefront" role="img" aria-label="Photo of the store building and its interior"></div>
  <div class="abs address-box display">4817 N 19th Street,<br>Milwaukee,<br>Wisconsin 53209</div>
  <div class="abs location-box display">
    <div class="l1">Our Location:</div>
    <div class="l2">2 Blocks</div>
    <div class="l3">North of 19th &amp;</div>
    <div class="l4">Pemberly</div>
  </div>
  <h1 class="abs accessory-headline display">
    <span class="big">Cellular</span><br>
    <span class="big">Accessory</span><br>
    <span class="mid">Superstore with</span><br>
    <span class="dark">1,000's of Case</span>
  </h1>
  <div class="photo case-photo" role="img" aria-label="Photo of a rugged phone case"></div>
  <div class="abs accessory-copy">
    <h3>Every accessory for every phone, all the time</h3>
    <p>Cases, chargers, screen guards and cables for every make and model. Stop in and browse our full wall of brand name and budget picks today.</p>
  </div>
  <div class="abs brand-list">
    <span class="brand"><i></i>Heron Shell</span>
    <span class="brand">Skinmitten</span>
    <span class="brand">Valdoro</span>
    <span class="brand">Cragmore</span>
  </div>
  <div class="abs band">
    <div class="abs site display">handsetfixitcrew.example</div>
    <div class="abs phone-block display">
      <div class="label">Phone Repair</div>
      <div class="number">414 - 555 - 0187</div>
    </div>
  </div>
</section>

<section class="flyer flyer--repair">
  <div class="abs logo"><i></i>Handset Fixit Crew</div>
  <h1 class="abs repair-headline display">
    <span class="small">Get your phone</span><br>
    <span class="huge">Fixed</span><br>
    <span class="huge">Today</span>
  </h1>
  <div class="photo handsets-photo" role="img" aria-label="Photo of several smartphones"></div>
  <div class="abs repair-copy">
    <p class="intro">We repair a wide range of cellular phones from Zelphones to Zelpads, Varnok's, QT's, Brivanta, and PWD</p>
    <h3>We fix all makes and models</h3>
    <p>If you carry a cell phone, we can repair it, from cracked screens to dead ports.</p>
    <h3>Professional on-site technicians</h3>
    <p>Trained technicians work in the store, so most repairs are done the same day.</p>
  </div>
  <div class="photo phones-photo" role="img" aria-label="Photo of two smartphones, one with a cracked screen"></div>
  <div class="abs buy-banner">We buy used and broken smart phones</div>
  <div class="abs badge">Repairs done on site with Certified Technicians</div>
  <div class="photo hand-photo" role="img" aria-label="Photo of a technician repairing a phone circuit board"></div>
  <ul class="abs service-list">
    <li><svg width="11" height="11" viewBox="0 0 11 11"><path d="M1 10 L6 5" stroke="#3f7fd6" stroke-width="2"/><circle cx="8" cy="3" r="2.5" fill="#3f7fd6"/></svg>Broken glass and LCDs</li>
    <li><svg width="11" height="11" viewBox="0 0 11 11"><path d="M1 10 L6 5" stroke="#3f7fd6" stroke-width="2"/><circle cx="8" cy="3" r="2.5" fill="#3f7fd6"/></svg>Battery replacement and charging port</li>
    <li><svg width="11" height="11" viewBox="0 0 11 11"><path d="M1 10 L6 5" stroke="#3f7fd6" stroke-width="2"/><circle cx="8" cy="3" r="2.5" fill="#3f7fd6"/></svg>Camera and home button replacement</li>
    <li><svg width="11" height="11" viewBox="0 0 11 11"><path d="M1 10 L6 5" stroke="#3f7fd6" stroke-width="2"/><circle cx="8" cy="3" r="2.5" fill="#3f7fd6"/></svg>Water damage</li>
  </ul>
  <div class="abs band">
    <div class="abs repair-phone display">
      <div class="label">Phone Repair</div>
      <div class="number">414 - 555 - 0187</div>
    </div>
  </div>
</section>

</body>
</html>
```